Wheels Open Doors - Two sided invitation to encourage bike friendly businesses

Pedal Haven is a charitable trust who want to grow everyday bike use. One way to do that is help businesses understand that 'Wheels Open Doors'. We want a postcard sized 'invitation' that bike users can give to their favourite businesses, inviting them to find out more about all the benefits of attracting bike users to their business and becoming a 'Pedal Haven Business'. We are currently finalising copy, so the attached is indicative but not final copy. The docx file is the words, the png is indicative of the type of infographic we might want to feature.
I'm also attaching a mock up of our window sticker for businesses, and some social shares featuring photographic images which we have available to use. This will give you an idea of our branding to date. Our extended branding concept (which we will use when we re-do our website) is based on icons, so I'm open to seeing icon focused designs also.
The feel needs to be inviting, credible, enticing, business like, noticeable, with a strong call to action.

Target Market(s)

Small business operators: retail, cafes, etc; also managers of larger chains such as supermarkets, gyms, etc.

Industry/Entity Type

Non Profit

Font styles to use
Serif
Other font styles liked:
• Logo is done in Raleway, so need compatible font.

Colors
9ccb3b

Requirements
Must have
• Two Sides
• Use the copy provided
• Strong call to action - visiting website
• Use our colours
• A6 sized cards
Nice to have
• Compelling images and/or infographic
• Consistency with circles / curves used in other branding.
Should not have
• Not bland, not something that will get lost on the recipients desk or counter.

```html
<!DOCTYPE html>
<html lang="en">
<head>
<meta charset="utf-8">
<title>Pedal Haven – Invitation Card</title>
<link rel="stylesheet" href="https://fonts.googleapis.com/css2?family=Raleway:wght@300;400;600;700&family=Bebas+Neue&display=swap">
<style>
  :root {
    --green: #3db54a;
    --green-deep: #2f9e3c;
    --green-soft: #55c060;
    --paper: #ebebeb;
    --paper-light: #f6f6f6;
    --ink: #3a3a3a;
    --white: #ffffff;
    --orange: #fbb040;
    --grey: #8a8a8a;
    --sky: #29b6d8;
    --stage: #d9d6d2;
  }
  * { box-sizing: border-box; margin: 0; padding: 0; }
  html, body { width: 874px; height: 1200px; overflow: hidden; }
  body {
    background: var(--stage);
    font-family: 'Raleway', sans-serif;
    position: relative;
  }
  .card {
    position: absolute;
    left: 86px;
    width: 696px;
    height: 492px;
    background: var(--paper);
    overflow: hidden;
    box-shadow: 0 4px 14px rgba(0,0,0,0.25);
  }
  .card--front { top: 70px; }
  .card--back { top: 626px; }
  .card svg.backdrop { position: absolute; inset: 0; }
  .abs { position: absolute; }

  /* Front */
  .headline {
    left: 26px; top: 32px; width: 300px;
    color: var(--white); font-weight: 600; font-size: 21px; line-height: 30px;
  }
  .pledge {
    left: 26px; top: 138px;
    color: var(--white); font-family: 'Bebas Neue', sans-serif; font-size: 30px; letter-spacing: 0.2px;
  }
  .photo-ring {
    left: 266px; top: 10px; width: 424px; height: 424px; border-radius: 50%;
    background: var(--paper-light);
  }
  .photo {
    left: 282px; top: 26px; width: 392px; height: 392px; border-radius: 50%;
    background: radial-gradient(circle at 50% 35%, #c9b7a0 0%, #8f7f86 45%, #5b6f8a 100%);
  }
  .question {
    left: 26px; top: 272px; color: var(--ink); font-size: 27px; font-weight: 600; line-height: 37px;
  }
  .stat {
    width: 128px; height: 128px; border-radius: 50%; border: 5px solid var(--white);
    color: var(--white); display: flex; flex-direction: column; align-items: center; justify-content: center;
    font-size: 18px; text-align: center; line-height: 22px;
  }
  .stat svg { margin-bottom: 8px; }
  .stat--bike { left: 284px; top: 302px; background: var(--orange); }
  .stat--freq { left: 418px; top: 342px; width: 122px; height: 122px; background: var(--grey); }
  .stat--car  { left: 554px; top: 300px; background: var(--sky); }
  .brand { display: flex; align-items: center; gap: 12px; }
  .brand__mark { border-radius: 50%; border: 4px solid #5a5a5a; background: var(--white); }
  .brand__name { color: var(--green); font-weight: 600; }
  .brand--front { left: 28px; top: 376px; }
  .brand--front .brand__mark { width: 100px; height: 100px; }
  .brand--front .brand__name { font-size: 26px; line-height: 26px; }
  .url { right: 14px; top: 466px; font-size: 13px; color: var(--ink); }

  /* Back */
  .back-title {
    left: 0; width: 696px; top: 28px; text-align: center;
    color: var(--white); font-weight: 700; font-size: 27px;
  }
  .reason { display: flex; align-items: flex-start; gap: 12px; color: var(--white); font-weight: 300; font-size: 16px; line-height: 20px; }
  .reason__icon {
    flex: none; width: 52px; height: 52px; border-radius: 50%; background: var(--white);
    display: flex; align-items: center; justify-content: center; margin-top: 2px;
  }
  .reason p { width: 170px; }
  .r1 { left: 14px; top: 82px; }
  .r2 { left: 225px; top: 82px; }
  .r3 { left: 457px; top: 82px; }
  .r3 p { width: 176px; }
  .r4 { left: 104px; top: 173px; }
  .r5 { left: 352px; top: 173px; }
  .r5 p { width: 190px; }
  .study {
    left: 0; width: 696px; top: 340px; text-align: center;
    color: var(--ink); font-size: 16px; line-height: 20px;
  }
  .think {
    left: 0; width: 696px; top: 390px; text-align: center;
    color: var(--green); font-size: 16px;
  }
  .brand--back { left: 103px; top: 422px; }
  .brand--back .brand__mark { width: 56px; height: 56px; border-width: 3px; }
  .brand--back .brand__name { font-size: 15px; }
  .cta { left: 240px; top: 430px; color: var(--ink); font-size: 15px; line-height: 20px; }
  .cta strong { font-weight: 600; }
</style>
</head>
<body>

<section class="card card--front">
  <svg class="backdrop" width="696" height="492" viewBox="0 0 696 492">
    <path d="M0 0 H696 V154 L520 300 L310 268 Q140 240 0 162 Z" fill="var(--green)"/>
    <path d="M0 162 Q140 240 310 268" fill="none" stroke="var(--paper-light)" stroke-width="6"/>
  </svg>
  <p class="abs headline">Why make biking customers and their $$$ – welcome at your business?</p>
  <p class="abs pledge">PLEDGE YOUR SUPPORT</p>
  <div class="abs photo-ring"></div>
  <div class="abs photo" role="img" aria-label="Photo of two smiling cyclists in helmets riding along a colourful city laneway"></div>
  <p class="abs question">HOW MUCH?<br>HOW OFTEN?</p>

  <div class="abs stat stat--bike">
    <svg width="72" height="40" viewBox="0 0 72 40" fill="none" stroke="#fff" stroke-width="3" stroke-linecap="round" stroke-linejoin="round">
      <circle cx="14" cy="26" r="11"/><circle cx="58" cy="26" r="11"/>
      <path d="M14 26 L26 8 H48 L58 26 M26 8 L36 26 L48 8 M22 3 H30 M48 8 L45 2 H52"/>
    </svg>
    <span>79% - $43</span>
  </div>
  <div class="abs stat stat--freq">
    <svg width="38" height="40" viewBox="0 0 38 40">
      <rect x="2" y="6" width="34" height="32" rx="3" fill="#fff"/>
      <rect x="9" y="1" width="4" height="9" rx="1" fill="#fff"/><rect x="25" y="1" width="4" height="9" rx="1" fill="#fff"/>
      <g fill="var(--grey)">
        <rect x="7" y="16" width="5" height="4"/><rect x="14" y="16" width="5" height="4"/><rect x="21" y="16" width="5" height="4"/><rect x="28" y="16" width="4" height="4"/>
        <rect x="7" y="23" width="5" height="4"/><rect x="14" y="23" width="5" height="4"/><rect x="21" y="23" width="5" height="4"/><rect x="28" y="23" width="4" height="4"/>
        <rect x="7" y="30" width="5" height="4"/><rect x="14" y="30" width="5" height="4"/>
      </g>
    </svg>
    <span>weekly<br>or more</span>
  </div>
  <div class="abs stat stat--car">
    <svg width="80" height="32" viewBox="0 0 80 32">
      <path d="M4 22 Q4 14 14 13 L24 4 H52 L64 13 Q76 14 76 22 V25 H4 Z" fill="#fff"/>
      <path d="M28 7 H40 V13 H21 Z M44 7 H51 L59 13 H44 Z" fill="var(--sky)"/>
      <circle cx="20" cy="25" r="6" fill="#fff" stroke="var(--sky)" stroke-width="2.5"/>
      <circle cx="60" cy="25" r="6" fill="#fff" stroke="var(--sky)" stroke-width="2.5"/>
    </svg>
    <span>66% - $44</span>
  </div>

  <div class="abs brand brand--front">
    <div class="brand__mark"></div>
    <span class="brand__name">Pedal Haven</span>
  </div>
  <p class="abs url">www.pedalhaven.org</p>
</section>

<section class="card card--back">
  <svg class="backdrop" width="696" height="492" viewBox="0 0 696 492" role="img" aria-label="Green tinted photo of a cyclist on a city street">
    <defs>
      <linearGradient id="backGreen" x1="0" y1="0" x2="1" y2="1">
        <stop offset="0" stop-color="var(--green-soft)"/>
        <stop offset="1" stop-color="var(--green-deep)"/>
      </linearGradient>
    </defs>
    <path d="M0 232 Q348 400 696 232 V250 Q348 418 0 250 Z" fill="var(--paper-light)"/>
    <path d="M0 0 H696 V222 Q348 390 0 222 Z" fill="url(#backGreen)"/>
  </svg>
  <h2 class="abs back-title">WHY WELCOME BIKES?</h2>

  <div class="abs reason r1">
    <div class="reason__icon"><svg width="26" height="30" viewBox="0 0 26 30"><path d="M9 2 H17 L15 7 H11 Z" fill="#444"/><path d="M11 8 H15 Q25 14 24 23 Q23 29 13 29 Q3 29 2 23 Q1 14 11 8 Z" fill="#444"/><text x="13" y="25" text-anchor="middle" font-size="13" font-weight="700" fill="#fff" font-family="Raleway, sans-serif">$</text></svg></div>
    <p>Biking customers spend $$$ where parking's easy.</p>
  </div>
  <div class="abs reason r2">
    <div class="reason__icon"><svg width="24" height="28" viewBox="0 0 24 28"><rect x="2" y="8" width="20" height="19" fill="#444"/><path d="M7 10 V5 Q12 0 17 5 V10" fill="none" stroke="#444" stroke-width="2"/></svg></div>
    <p>They spend $$$ locally as they must carry what they buy.</p>
  </div>
  <div class="abs reason r3">
    <div class="reason__icon"><svg width="34" height="26" viewBox="0 0 34 26" fill="none" stroke="#444" stroke-width="2" stroke-linecap="round"><circle cx="8" cy="18" r="6"/><circle cx="26" cy="18" r="6"/><path d="M8 18 L14 10 H22 L26 18 M14 10 L18 18"/><circle cx="17" cy="3" r="2.5" fill="#444"/></svg></div>
    <p>Biking customers move slower, so see what your business offers.</p>
  </div>
  <div class="abs reason r4">
    <div class="reason__icon"><svg width="32" height="22" viewBox="0 0 32 22" fill="#444"><circle cx="9" cy="6" r="4"/><circle cx="23" cy="6" r="4"/><circle cx="16" cy="8" r="5"/><path d="M2 22 Q2 12 9 12 Q13 12 14 15 Q16 13 18 15 Q19 12 23 12 Q30 12 30 22 Z"/></svg></div>
    <p>They tell friends where's good to park and shop, where they feel welcome.</p>
  </div>
  <div class="abs reason r5">
    <div class="reason__icon"><svg width="30" height="28" viewBox="0 0 30 28"><path d="M15 26 L4 14 Q-1 7 5 3 Q11 0 15 6 Q19 0 25 3 Q31 7 26 14 Z" fill="none" stroke="#444" stroke-width="2.2" stroke-linejoin="round"/></svg></div>
    <p>You're helping people be environmentally, budget and heart friendly – and they'll you for it.</p>
  </div>

  <p class="abs study">A Melbourne study showed swapping a car park for six bike parks could<br>increase the space's retail spend from $27 to $97.20 an hour.</p>
  <p class="abs think">Just think – every bike parked by someone else's business could have been your customer.</p>
  <div class="abs brand brand--back">
    <div class="brand__mark"></div>
  </div>
  <p class="abs cta">See <strong>pedalhaven.org.nz</strong><br>to see how you can become a pedal haven business.</p>
  <span class="abs brand__name" style="left:166px; top:440px; font-size:14px; width:70px; line-height:16px;">Pedal Haven</span>
</section>

</body>
</html>
```